AMBER HARBOUR WEB

We need a home design in wordpress, we have now a web but we would like to improve it. Our current web is www.amberharbourvillas.example Our business is holliday rental of villas in Ibiza. Our guest must know that we are a reliable company, professional and with experience and good reviews. We want them to click in our reservation engine: https://bookings.amberharbourvillas.example/en/ and make reservation in our website. We would also like to say that all the properties that we have are just us who commercialize so we have best price available. Many people are going to see our villas in staylodgr.example and look to our website to make a reservation with us so we need to show them that they are at the right place and click at our link to our reservation engine. What make us special is that we are a local company, we are from Ibiza, Our guests are always received in person by the Amber Harbour Villas team. You will enjoy extensive tourist information when you check in and during the entire stay. You will be attended by ChatPelt and calls, always happy to help so that you have a happy and fun stay! Our guest stay is better than in hotel as they have more spece, private swiming pool, private garden, barbeque ... To rent a villa is the best way to stay in Ibiza. We also have a promotional video: https://vidshare.example/Qm7pTz3RxLa Let our philosophy be shown, we think that coming on holiday to Ibiza implies seeing the nature that we have in Ibiza, hence our name AMBER HARBOUR, like the pins that almost touch the sea in Ibiza, or the posidonea meadows where the intense green of the seaweed and the blue of the sea. We are aware of the environment, and we love Ibiza. For us, the client who visits Ibiza, should rent a car, go around the island, eat in a restaurant one day in front of the sea, is a night of partying to the discs, go shopping, visit the ancient heritage of Umanity, make some aquatic sport, enjoy the pool, those are for us Ibiza.

Target Market(s)

Europe, people from Holand, UK, Germany, France, Spain ...

Industry/Entity Type

Tourism

Colors

Designer to choose colors to be used in the design.

Requirements
Must have
• Pictures of Ibiza.
Nice to have
• Our name Amber Harbour Villas is beacuse in Ibiza there is forest that almost touch the watter of the Mediterranean sea, so you can see green of the forest and blue of the sea and the sky. And also beacause under the watter of the sea there is a plant called Posidonia that is also green please see the picture of posidonia.

```html
<!DOCTYPE html>
<html lang="en">
<head>
<meta charset="utf-8">
<title>Amber Harbour Villas Ibiza</title>
<link rel="stylesheet" href="https://fonts.googleapis.com/css2?family=Cinzel:wght@400;600;700&family=Montserrat:wght@500;600;800&family=Quicksand:wght@400;500;600&display=swap">
<style>
:root{
  --green-dark:#5b8a35;
  --green-mid:#6f9a3c;
  --lime:#a6c83a;
  --blue:#2ea0d8;
  --text:#555;
  --heading:#5e8a2f;
  --footer:#141414;
  --white:#fff;
}
*{box-sizing:border-box;margin:0;padding:0}
html,body{width:1200px;height:3870px;overflow:hidden}
body{position:relative;font-family:'Quicksand',sans-serif;color:var(--text);background:var(--white)}
.abs{position:absolute}
.btn{position:absolute;display:flex;align-items:center;justify-content:center;color:var(--white);font-family:'Cinzel',serif;font-size:21px;letter-spacing:1px;background:linear-gradient(90deg,var(--lime),var(--blue));border-radius:4px}
.heading{position:absolute;left:0;width:1200px;text-align:center;font-family:'Cinzel',serif;font-weight:600}

/* top bar */
.topbar{left:0;top:0;width:1200px;height:41px;background:var(--green-dark)}
.topbar__phone{left:796px;top:10px;color:var(--white);font-family:'Montserrat',sans-serif;font-size:15px;display:flex;align-items:center;gap:8px}
.topbar__book{left:976px;top:0;width:147px;height:53px;border-radius:0 0 10px 10px;font-size:18px;background:linear-gradient(90deg,var(--lime),var(--blue))}

/* header */
.brand{display:flex;align-items:center;gap:12px;font-family:'Cinzel',serif;font-weight:600;color:var(--green-dark)}
.brand__dot{width:22px;height:22px;border-radius:50%;background:var(--green-dark)}
.header__brand{left:78px;top:68px;font-size:28px}
.nav{left:0;top:83px;font-family:'Montserrat',sans-serif;font-size:13.5px;color:#333}
.nav span{position:absolute;white-space:nowrap}
.nav .active{color:var(--lime)}
.nav .active::after{content:"";position:absolute;left:0;right:18px;top:22px;height:2px;background:var(--lime)}

/* hero */
.hero{left:0;top:131px;width:1200px;height:545px;background:linear-gradient(180deg,#7fb6dc 0%,#6e9a58 30%,#b38d63 62%,#8a6a4c 100%)}
.hero__panel{left:0;top:335px;width:575px;height:158px;background:rgba(30,30,30,.6);border-right:6px solid var(--green-dark)}
.hero__title{left:77px;top:368px;color:var(--white);font-family:'Montserrat',sans-serif;font-weight:800;font-size:41px;line-height:47px}
.hero__dots{left:1152px;top:358px;display:flex;flex-direction:column;gap:8px}
.hero__dots i{width:16px;height:16px;border-radius:50%;background:var(--white);display:block}
.hero__dots i.on{background:var(--lime)}

/* search */
.search{left:107px;top:598px;width:985px;height:195px;background:var(--white);border-top:4px solid var(--lime);box-shadow:0 4px 16px rgba(0,0,0,.15)}
.search__title{left:138px;top:626px;font-family:'Cinzel',serif;font-weight:600;font-size:28px;color:var(--heading)}
.search__sub{left:141px;top:665px;font-size:14px}
.field{position:absolute;top:706px;height:51px;border:1px solid #ccc;border-radius:4px;background:#f6f6f6;display:flex;align-items:center;gap:8px;padding-left:14px;font-size:13.5px;color:#555}
.field svg{flex:none}

/* intro */
.mark{position:absolute;left:588px;width:24px;height:24px;border-radius:50%;background:var(--green-dark)}
.intro__h1{top:932px;font-size:43px;color:var(--heading)}
.intro__h2{top:982px;font-size:32px;color:var(--lime)}
.intro__text{left:240px;top:1041px;width:721px;text-align:center;font-size:14px;line-height:27px}
.intro__text p{margin-bottom:14px}

/* accommodation */
.accom{left:0;top:1421px;width:1200px;height:542px;background:var(--green-mid)}
.accom__h1{top:1480px;font-size:43px;color:var(--white)}
.accom__h2{top:1532px;font-size:29px;color:var(--lime)}
.card__img{position:absolute;top:1612px;width:328px;height:198px}
.card__cap{position:absolute;top:1810px;width:317px;height:78px;background:var(--white);padding:18px 0 0 28px}
.card__cap b{display:block;font-family:'Montserrat',sans-serif;font-weight:600;font-size:18px;color:#222}
.card__cap small{font-size:13.5px;color:#555}
.card__cap svg{position:absolute;right:24px;top:19px}
.chev{position:absolute}

/* video */
.video__h{top:2018px;font-size:40px;color:var(--heading)}
.skyline{left:0;top:2500px;width:1200px;height:156px;background:linear-gradient(180deg,#fff,#ececec)}
.video{left:246px;top:2097px;width:708px;height:416px;background:radial-gradient(ellipse at 50% 60%,#f08a2a 0%,#a04820 35%,#2d1a14 75%)}
.video__play{left:564px;top:2274px}

/* testimonials */
.reviews{left:0;top:2656px;width:1200px;height:437px;background:linear-gradient(90deg,#a7c93c 0%,#8db33e 50%,#5f8f3a 100%)}
.reviews__h{top:2706px;font-size:40px;color:var(--white)}
.quote{left:566px;top:2779px;width:68px;height:68px;border-radius:50%;background:var(--white)}
.reviews__text{left:312px;top:2876px;width:576px;text-align:center;color:var(--white);font-style:italic;font-size:15.5px;line-height:27px}
.reviews__name{left:0;top:2977px;width:1200px;text-align:center;color:var(--white);font-family:'Montserrat',sans-serif;font-weight:500;font-size:17px}
.avatar{position:absolute;border-radius:50%;border:4px solid var(--white)}

/* newsletter */
.save__h{top:3306px;font-size:40px;color:var(--heading)}
.save__sub{left:0;top:3363px;width:1200px;text-align:center;font-size:15px;color:#333}
.save__input{left:243px;top:3418px;width:520px;height:52px;border:1px solid #ccc;border-radius:4px;padding:17px 0 0 18px;font-size:13.5px;color:#888}

/* footer */
.footer{left:0;top:3536px;width:1200px;height:273px;background:var(--footer)}
.footer__brand{left:78px;top:3650px;font-size:24px}
.footer__h{position:absolute;top:3564px;font-family:'Cinzel',serif;font-size:19px;color:var(--green-mid)}
.footer__list{left:345px;top:3614px;list-style:none;font-size:13.5px;color:#ccc}
.footer__list li{height:33px;position:relative;padding-left:16px}
.footer__list li::before{content:"";position:absolute;left:0;top:6px;width:6px;height:6px;border-radius:50%;background:var(--lime)}
.contact{position:absolute;left:608px;display:flex;gap:16px;font-size:13.5px;color:#ccc;line-height:23px}
.social{position:absolute;left:886px;display:flex;align-items:center;gap:16px;font-size:13.5px;color:#ccc}
.social i{width:42px;height:42px;border-radius:50%;display:block}
.copy{left:0;top:3809px;width:1200px;height:61px;background:var(--green-mid);color:#e8f0dc;text-align:center;line-height:61px;font-size:13.5px}
</style>
</head>
<body>

<div class="abs topbar"></div>
<div class="abs topbar__phone">
  <svg width="22" height="22" viewBox="0 0 22 22"><circle cx="11" cy="11" r="10" fill="none" stroke="#a6c83a" stroke-width="2"/><path d="M8 6l2 3-1.5 1.5c.7 1.5 1.8 2.6 3.3 3.3L13.3 12l3 2-1.3 2c-4.5-.3-8.3-4-8.6-8.6z" fill="#a6c83a"/></svg>
  +34 600 112 358
</div>
<div class="btn topbar__book">BOOK IBIZA</div>

<div class="abs brand header__brand"><span class="brand__dot"></span>AMBER HARBOUR</div>
<nav class="abs nav">
  <span class="active" style="left:523px">HOME</span>
  <span style="left:601px">EXPERIENCE</span>
  <span style="left:718px">ABOUT US</span>
  <span style="left:819px">CONTACT US</span>
  <span style="left:942px">ALL PROPERTIES</span>
  <span style="left:1078px;top:-2px"><svg width="40" height="20" viewBox="0 0 40 20"><circle cx="10" cy="9" r="9" fill="#3c5aa6"/><path d="M10 0a9 9 0 0 1 9 9H10z" fill="#d33"/><path d="M26 6l4 4 4-4" fill="none" stroke="#777" stroke-width="1.5"/></svg></span>
</nav>

<div class="abs hero" role="img" aria-label="Photo of an Ibiza villa pool terrace with driftwood sculpture, pine trees and the Mediterranean sea"></div>
<div class="abs hero__panel"></div>
<h1 class="abs hero__title">THE BEST WAY TO<br>STAY IN IBIZA !</h1>
<div class="abs hero__dots"><i></i><i></i><i class="on"></i><i></i><i></i></div>

<section class="abs search"></section>
<h2 class="abs search__title">FIND DEALS FOR ANY SEASON</h2>
<p class="abs search__sub">From cozy country homes to funky city apartments</p>
<div class="field" style="left:141px;width:313px"><svg width="18" height="16" viewBox="0 0 18 16"><path d="M3 6l2-5h8l2 5h1v6h-2v3h-2v-3H6v3H4v-3H2V6z" fill="#777"/></svg>Best Available Rate</div>
<div class="field" style="left:464px;width:218px"><svg width="16" height="16" viewBox="0 0 16 16"><rect x="1" y="3" width="14" height="12" rx="1" fill="#777"/><rect x="3" y="7" width="10" height="6" fill="#f6f6f6"/><rect x="4" y="1" width="2" height="4" fill="#777"/><rect x="10" y="1" width="2" height="4" fill="#777"/></svg>Check-in &nbsp;- &nbsp;Check-out</div>
<div class="field" style="left:691px;width:218px"><svg width="16" height="16" viewBox="0 0 16 16"><circle cx="8" cy="5" r="4" fill="#777"/><path d="M1 16c0-5 3-7 7-7s7 2 7 7z" fill="#777"/></svg>2 adults &nbsp;- &nbsp;0 kids</div>
<div class="btn" style="left:918px;top:706px;width:141px;height:51px">BOOK</div>

<span class="mark" style="top:866px"></span>
<h2 class="heading intro__h1">Villas and the Countryside The</h2>
<h3 class="heading intro__h2">Best option to stay in Ibiza</h3>
<div class="abs intro__text">
  <p>Amber Harbour Villas is a company specialized in offering its clients accommodation in Villas on the countryside of Ibiza. Our guests enjoy the rural Ibiza, tranquility, relax, private pool, close to dream beaches and coves, the best restaurants, an unforgettable holiday for family or friends.</p>
  <p>Every day can be a different experience, beach, restaurant, flea market, disco, hiking, kayaking, horseback riding, shopping, history, boat ride! There is a lot of variety for all budgets!</p>
  <p>The maximum distances of the island are 41 kilometers from north to south and 15 kilometers from east to west, we always recommend renting a car. Enjoy the freedom to go where you prefer, without depending on schedules or public transportation.</p>
</div>
<div class="btn" style="left:506px;top:1307px;width:188px;height:52px">LEARN MORE</div>

<section class="abs accom"></section>
<h2 class="heading accom__h1">Whatever accommodations you’re</h2>
<h3 class="heading accom__h2">looking for, we’ve got them...</h3>
<svg class="chev" style="left:32px;top:1723px" width="20" height="44" viewBox="0 0 20 44"><path d="M18 2L3 22l15 20" fill="none" stroke="#c6dc8a" stroke-width="2.5"/></svg>
<svg class="chev" style="left:1154px;top:1723px" width="20" height="44" viewBox="0 0 20 44"><path d="M2 2l15 20L2 42" fill="none" stroke="#c6dc8a" stroke-width="2.5"/></svg>

<div class="card__img" style="left:77px;background:linear-gradient(180deg,#6fb6e6 0%,#3fa9c9 50%,#8c6b4a 100%)" role="img" aria-label="Photo of a glamping trailer on a seaside deck with sun loungers"></div>
<div class="card__cap" style="left:82px"><b>Glamping</b><small>8,577 Glamping Sites</small>
<svg width="40" height="40" viewBox="0 0 40 40"><circle cx="20" cy="20" r="17" fill="none" stroke="#a6c83a" stroke-width="4"/><path d="M11 20h16M21 13l7 7-7 7" fill="none" stroke="#2ea0d8" stroke-width="4"/></svg></div>

<div class="card__img" style="left:436px;background:linear-gradient(180deg,#8fa9cc 0%,#6b4a30 55%,#dfe6ee 100%)" role="img" aria-label="Photo of a wooden chalet in the snow at dusk"></div>
<div class="card__cap" style="left:441px"><b>Cabins</b><small>12,643 cabins</small>
<svg width="40" height="40" viewBox="0 0 40 40"><circle cx="20" cy="20" r="17" fill="none" stroke="#a6c83a" stroke-width="4"/><path d="M11 20h16M21 13l7 7-7 7" fill="none" stroke="#2ea0d8" stroke-width="4"/></svg></div>

<div class="card__img" style="left:796px;background:linear-gradient(180deg,#cfe0c0 0%,#8a7a66 45%,#6d6a5c 100%)" role="img" aria-label="Photo of a stone cottage with a small garden courtyard"></div>
<div class="card__cap" style="left:801px"><b>Cottages</b><small>125,347 cottages</small>
<svg width="40" height="40" viewBox="0 0 40 40"><circle cx="20" cy="20" r="17" fill="none" stroke="#a6c83a" stroke-width="4"/><path d="M11 20h16M21 13l7 7-7 7" fill="none" stroke="#2ea0d8" stroke-width="4"/></svg></div>

<h2 class="heading video__h">Watch Our Video</h2>
<div class="abs skyline" role="img" aria-label="Faint line drawing of a city skyline"></div>
<div class="abs video" role="img" aria-label="Promotional video still of a person silhouetted against an Ibiza sunset over the sea"></div>
<svg class="abs video__play" width="72" height="72" viewBox="0 0 72 72" aria-label="Play video"><circle cx="36" cy="36" r="34" fill="rgba(255,255,255,.9)" stroke="#a6c83a" stroke-width="3"/><path d="M29 22l22 14-22 14z" fill="#5b8a35"/></svg>
<div class="btn" style="left:506px;top:2540px;width:188px;height:51px">BOOK NOW</div>

<section class="abs reviews" role="img" aria-label="Photo of a happy family on holiday, tinted green"></section>
<h2 class="heading reviews__h">What Our Client Say</h2>
<div class="abs quote"></div>
<svg class="abs" style="left:587px;top:2801px" width="26" height="22" viewBox="0 0 26 22"><path d="M0 22V11C0 4 4 0 10 0v4c-3 0-5 2-5 6h5v12zM15 22V11c0-7 4-11 10-11v4c-3 0-5 2-5 6h5v12z" fill="#2ea0d8"/></svg>
<svg class="chev" style="left:178px;top:2884px" width="20" height="44" viewBox="0 0 20 44"><path d="M18 2L3 22l15 20" fill="none" stroke="#fff" stroke-width="2"/></svg>
<svg class="chev" style="left:990px;top:2884px" width="20" height="44" viewBox="0 0 20 44"><path d="M2 2l15 20L2 42" fill="none" stroke="#fff" stroke-width="2"/></svg>
<p class="abs reviews__text">We Had a brilliant time at Can Serra, Marisol our host was so helpful and the villa was wonderful... Everything we needed was there and the pool was wonderful !</p>
<p class="reviews__name abs">Can Serra Llevant</p>
<div class="avatar" style="left:432px;top:3043px;width:94px;height:94px;background:linear-gradient(160deg,#9fc8e8,#c69a7a)" role="img" aria-label="Guest photo of two friends"></div>
<div class="avatar" style="left:541px;top:3032px;width:118px;height:118px;background:linear-gradient(160deg,#bcd8f0,#3f6e9e)" role="img" aria-label="Guest photo of a traveller on a mountain"></div>
<div class="avatar" style="left:673px;top:3043px;width:94px;height:94px;background:linear-gradient(160deg,#d8c4b0,#6a4a3a)" role="img" aria-label="Guest photo of a smiling woman"></div>

<span class="mark" style="top:3240px"></span>
<h2 class="heading save__h">Save Time, Save Money!</h2>
<p class="abs save__sub">Sign up and we'll send the best deals to you</p>
<div class="abs save__input">Enter Email *</div>
<div class="btn" style="left:770px;top:3418px;width:187px;height:52px">BOOK NOW</div>

<footer class="abs footer"></footer>
<div class="abs brand footer__brand"><span class="brand__dot"></span>AMBER HARBOUR</div>
<h4 class="footer__h" style="left:342px">Sitemap</h4>
<ul class="abs footer__list"><li>Home</li><li>Experience</li><li>About Us</li><li>Contact Us</li><li>All Properties</li></ul>
<h4 class="footer__h" style="left:608px">Contact Us</h4>
<div class="contact" style="top:3610px"><svg width="20" height="28" viewBox="0 0 20 28"><path d="M10 0a10 10 0 0 1 10 10c0 7-10 18-10 18S0 17 0 10A10 10 0 0 1 10 0z" fill="#a6c83a"/><circle cx="10" cy="10" r="4" fill="#141414"/></svg><span>Carrer del Faro, 7,<br>Cala Serena,<br>07899, IBIZA</span></div>
<div class="contact" style="top:3690px"><svg width="22" height="22" viewBox="0 0 22 22"><path d="M5 1l4 5-2.5 2.5c1.2 2.6 3.4 4.8 6 6L15 12l5 4-2 4C9 19.5 2.5 13 2 4z" fill="#a6c83a"/></svg><span>+34600112358</span></div>
<div class="contact" style="top:3736px"><svg width="22" height="18" viewBox="0 0 22 18"><rect width="22" height="18" rx="2" fill="#a6c83a"/><path d="M1 2l10 8 10-8" fill="none" stroke="#141414" stroke-width="2"/></svg><span>reservas@amberharbourvillas.example</span></div>
<h4 class="footer__h" style="left:886px">Follow Us</h4>
<div class="social" style="top:3610px"><i style="background:#3b5998"></i>Friendwall</div>
<div class="social" style="top:3662px"><i style="background:#1da1f2"></i>Chirper</div>
<div class="abs copy">©Amber Harbour - 2019 All Rights Resrerved.</div>

</body>
</html>
```